Design an Annual Report Template for Healthcare NGO

Template for Healthcare NGO Annual Report

An A4 full color, vertical format, print project. An annual report design template that will be used this year and in future years. The project must be provided is either InDesign or MS Publisher.

The design concept must be developed but my client has an existing logo, QR code, style guide including colors and fonts to be used available for download here: https://www.filevaultix.com/s/qw7rbn3plm2vz81/AnnualReportLogosBrand.zip

A good example (design standard and content wise) of what my client requires is located here: http://shrtlnkq.com/w3rvtaz

The final annual report may be approx. 20-40 pages based on this template but the concept design must already include pages/sections including:
front and back outside cover (QR code must be features)
front and back inside cover
content page
letter from the board chair (half page)
letter from the ceo (half page)
letter from the director (full page)
introduction page
what we do section
results section - highlighting 6 areas of acheivement (% number for each)
sub-brand one page
sub-brand two page
sub-brand three page
sub-brand four page
sub-brand five page
sub-brand six page
support section
parnters section
organisation chart (40 people)
transparency page
sustainabilty page
annual accounts and finance section

Stock photos can be included but he actual text, tables, graph and photo content will be added by us into your template later.

```html
<!DOCTYPE html>
<html lang="en">
<head>
<meta charset="utf-8">
<title>Annual Report – Contents</title>
<link rel="stylesheet" href="https://fonts.googleapis.com/css2?family=Open+Sans:wght@700&family=Source+Sans+3:wght@400&display=swap">
<style>
  :root {
    --green: #80bd41;
    --green-light: #9dcf65;
    --paper: #eeeeee;
    --ink: #1a1a1a;
    --white: #ffffff;
  }
  * { margin: 0; padding: 0; box-sizing: border-box; }
  html, body { width: 848px; height: 1200px; overflow: hidden; background: var(--paper); }
  .page {
    position: relative;
    width: 848px;
    height: 1200px;
    background: var(--paper);
    overflow: hidden;
  }
  .page-waves {
    position: absolute;
    inset: 0;
    width: 848px;
    height: 1200px;
  }
  .wave-dark { fill: var(--green); }
  .wave-light { fill: var(--green-light); }
  .page-title {
    position: absolute;
    top: 110px;
    left: 0;
    width: 848px;
    text-align: center;
    font-family: "Open Sans", sans-serif;
    font-weight: 700;
    font-size: 35px;
    letter-spacing: -0.5px;
    color: var(--white);
  }
  .toc {
    position: absolute;
    top: 363px;
    left: 191px;
    width: 459px;
    list-style: none;
    font-family: "Source Sans 3", sans-serif;
    font-size: 17.5px;
    color: var(--ink);
  }
  .toc-item {
    display: flex;
    align-items: center;
    height: 35.6px;
  }
  .toc-number { width: 38px; flex: none; }
  .toc-label { flex: none; }
  .toc-leader {
    flex: 1;
    margin: 0 20px 0 16px;
    border-bottom: 1px dashed var(--green);
    transform: translateY(1px);
  }
  .toc-page {
    flex: none;
    width: 20px;
    text-align: right;
    color: var(--green);
  }
</style>
</head>
<body>
<div class="page">
  <svg class="page-waves" viewBox="0 0 794 1123" preserveAspectRatio="none" aria-hidden="true">
    <path class="wave-light" d="M0,0 H794 V182 C520,180 220,250 0,366 Z"/>
    <path class="wave-dark" d="M0,0 H794 V160 C520,162 200,218 0,312 Z"/>
    <path class="wave-light" d="M290,1123 C480,1062 660,992 794,915 V1123 Z"/>
    <path class="wave-dark" d="M420,1123 C580,1072 700,1012 794,950 V1123 Z"/>
  </svg>

  <h1 class="page-title">CONTENT</h1>

  <ol class="toc">
    <li class="toc-item"><span class="toc-number">01.</span><span class="toc-label">Letter from the Board Chair</span><span class="toc-leader"></span><span class="toc-page">01</span></li>
    <li class="toc-item"><span class="toc-number">02.</span><span class="toc-label">Letter from the CEO</span><span class="toc-leader"></span><span class="toc-page">01</span></li>
    <li class="toc-item"><span class="toc-number">03.</span><span class="toc-label">Letter from the Director</span><span class="toc-leader"></span><span class="toc-page">02</span></li>
    <li class="toc-item"><span class="toc-number">04.</span><span class="toc-label">Introduction</span><span class="toc-leader"></span><span class="toc-page">03</span></li>
    <li class="toc-item"><span class="toc-number">05.</span><span class="toc-label">What we do</span><span class="toc-leader"></span><span class="toc-page">04</span></li>
    <li class="toc-item"><span class="toc-number">06.</span><span class="toc-label">Results</span><span class="toc-leader"></span><span class="toc-page">05</span></li>
    <li class="toc-item"><span class="toc-number">07.</span><span class="toc-label">Sub-Brand one</span><span class="toc-leader"></span><span class="toc-page">06</span></li>
    <li class="toc-item"><span class="toc-number">08.</span><span class="toc-label">Sub-Brand two</span><span class="toc-leader"></span><span class="toc-page">08</span></li>
    <li class="toc-item"><span class="toc-number">09.</span><span class="toc-label">Sub-Brand three</span><span class="toc-leader"></span><span class="toc-page">10</span></li>
    <li class="toc-item"><span class="toc-number">10.</span><span class="toc-label">Sub-Brand four</span><span class="toc-leader"></span><span class="toc-page">12</span></li>
    <li class="toc-item"><span class="toc-number">11.</span><span class="toc-label">Sub-Brand five</span><span class="toc-leader"></span><span class="toc-page">14</span></li>
    <li class="toc-item"><span class="toc-number">12.</span><span class="toc-label">Sub-Brand six</span><span class="toc-leader"></span><span class="toc-page">16</span></li>
    <li class="toc-item"><span class="toc-number">13.</span><span class="toc-label">Support</span><span class="toc-leader"></span><span class="toc-page">17</span></li>
    <li class="toc-item"><span class="toc-number">14.</span><span class="toc-label">Parnters</span><span class="toc-leader"></span><span class="toc-page">18</span></li>
    <li class="toc-item"><span class="toc-number">15.</span><span class="toc-label">Organisation Chart</span><span class="toc-leader"></span><span class="toc-page">19</span></li>
    <li class="toc-item"><span class="toc-number">16.</span><span class="toc-label">Transparency</span><span class="toc-leader"></span><span class="toc-page">20</span></li>
    <li class="toc-item"><span class="toc-number">17.</span><span class="toc-label">Sustainabilty</span><span class="toc-leader"></span><span class="toc-page">21</span></li>
    <li class="toc-item"><span class="toc-number">18.</span><span class="toc-label">Annual Accounts and Finance</span><span class="toc-leader"></span><span class="toc-page">22</span></li>
  </ol>
</div>
</body>
</html>
```